Greek Yogurt Design

Design Brief – Premium Greek Yogurt Line (150g Pot)
Background
We are a small-to-medium dairy producer launching a new premium Greek yogurt range. This line will come in slightly larger pots than our standard yogurts, and we are targeting an upmarket clientele with a higher price point.
Product Details
Product: Greek Yogurt (fruit on the bottom, yogurt on top)
Flavours:
Natural
Strawberry
Forest Fruit
Peach & Apricot
Vanilla
Mango
Weight: 150g
Kosher Certification: 2 logos must be applied neatly (logos provided).
Lid: Standard universal lid (not flavour-specific).
Design Style
Clean, elegant, and premium feel (avoid clutter).
Should stand out as sophisticated compared to our standard range.
Visual hierarchy:
Brand & product type (Greek Yogurt) should be clear.
Flavour indicated with subtle but distinct cues (colour palette, fruit illustration/photography).
“Fruit on the bottom” message should be communicated simply.
Premium cues: minimalist typography, restrained colour palette, elegant fruit imagery.
References / Inspiration
Velmora Yogurt
– clean, bold, dairy-traditional.
Brask Dairy Greek Style
– natural, elegant design.
Lunaro Greek Yogurt
– modern, colourful yet clean.
Deliverables
Pot sleeve / pot design (to wrap around container).
Must work across all flavours with colour/flavour variation.
Space for universal lid (do not design individual lids).
Application of 2 kosher logos in a balanced way.
Updates
Industry/Entity Type
Dairy
Colors
Designer to choose colors to be used in the design.
Look and feel
Each slider illustrates characteristics of the customer's brand and the style your logo design should communicate.

```html
<!DOCTYPE html>
<html lang="en">
<head>
<meta charset="utf-8">
<title>Oresta Greek Yogurt – Peach &amp; Apricot Pot Sleeve</title>
<link href="https://fonts.googleapis.com/css2?family=Baloo+2:wght@600;700&family=Courgette&display=swap" rel="stylesheet">
<style>
  :root {
    --stage: #868686;
    --sleeve: #f6eee9;
    --sleeve-edge: #ece1da;
    --green: #3fae3a;
    --gold: #d49a2e;
    --gold-rule: #d9a54a;
    --ink: #2a211c;
    --peach-1: #f6b64a;
    --peach-2: #e8742e;
    --peach-3: #c9462a;
  }
  * { box-sizing: border-box; margin: 0; padding: 0; }
  html, body { width: 1200px; height: 900px; overflow: hidden; }
  body {
    background: var(--stage);
    display: flex;
    align-items: center;
    justify-content: center;
  }
  .sleeve {
    position: relative;
    width: 560px;
    height: 740px;
    background: linear-gradient(90deg, var(--sleeve-edge), var(--sleeve) 18%, var(--sleeve) 82%, var(--sleeve-edge));
    border-radius: 6px;
    overflow: hidden;
  }
  .brand {
    position: absolute;
    top: 70px;
    left: 0; right: 0;
    display: flex;
    align-items: center;
    justify-content: center;
    gap: 16px;
    z-index: 2;
  }
  .brand-dot {
    width: 34px; height: 34px;
    border-radius: 50%;
    background: var(--green);
  }
  .brand-name {
    font-family: "Baloo 2", sans-serif;
    font-weight: 700;
    font-size: 92px;
    line-height: 1;
    color: var(--green);
  }
  .tagline {
    position: absolute;
    top: 186px;
    left: 0; right: 0;
    text-align: center;
    font-family: "Courgette", cursive;
    font-size: 26px;
    color: var(--green);
    z-index: 2;
  }
  .product-type {
    position: absolute;
    top: 256px;
    left: 0; right: 0;
    text-align: center;
    font-family: "Baloo 2", sans-serif;
    font-weight: 700;
    font-size: 96px;
    line-height: 0.95;
    color: var(--green);
    z-index: 2;
  }
  .flavour {
    position: absolute;
    top: 478px;
    left: 110px; right: 110px;
    text-align: center;
    z-index: 2;
  }
  .rule {
    height: 3px;
    background: linear-gradient(90deg, transparent, var(--gold-rule) 15%, var(--gold-rule) 85%, transparent);
  }
  .flavour-name {
    margin-top: 12px;
    font-family: "Courgette", cursive;
    font-size: 42px;
    line-height: 1.1;
    color: var(--gold);
  }
  .flavour-note {
    margin: 2px 0 12px;
    font-family: "Courgette", cursive;
    font-size: 24px;
    color: var(--ink);
  }
  .fruit {
    position: absolute;
    border-radius: 50%;
    background: radial-gradient(circle at 40% 40%, var(--peach-1), var(--peach-2) 70%, var(--peach-3));
    z-index: 1;
  }
  .fruit.half-a { left: 14px; top: 268px; width: 66px; height: 84px; }
  .fruit.slice-a { right: 16px; top: 290px; width: 48px; height: 92px; border-radius: 60% 40% 50% 50%; }
  .fruit.slice-b { left: 18px; top: 470px; width: 54px; height: 70px; border-radius: 50% 40% 60% 50%; }
  .fruit.half-b { right: -18px; top: 560px; width: 84px; height: 110px; }
  .fruit.half-c { left: 40px; top: 650px; width: 110px; height: 100px; }
  .fruit.slice-c { left: 250px; top: 675px; width: 140px; height: 70px; border-radius: 60% 60% 40% 40%; }
</style>
</head>
<body>
  <main class="sleeve">
    <div class="brand">
      <span class="brand-dot"></span>
      <span class="brand-name">Oresta</span>
    </div>
    <p class="tagline">Dairy Goodness</p>

    <h1 class="product-type">GREEK<br>YOGURT</h1>

    <div class="flavour">
      <div class="rule"></div>
      <p class="flavour-name">Peach &amp; Apricot</p>
      <p class="flavour-note">on the Bottom</p>
      <div class="rule"></div>
    </div>

    <div class="fruit half-a" role="img" aria-label="Photo of a halved peach with stone"></div>
    <div class="fruit slice-a" role="img" aria-label="Photo of a peach slice"></div>
    <div class="fruit slice-b" role="img" aria-label="Photo of a peach slice"></div>
    <div class="fruit half-b" role="img" aria-label="Photo of a halved peach with stone"></div>
    <div class="fruit half-c" role="img" aria-label="Photo of a halved peach with stone"></div>
    <div class="fruit slice-c" role="img" aria-label="Photo of a peach wedge"></div>
  </main>
</body>
</html>
```